Covert current Brochures from PDF to PDF editable, No need to change the format

We have 3 brochures that need to be updated in the template to make the content editable. No need to change the format.

```html
<!DOCTYPE html>
<html lang="en">
<head>
<meta charset="utf-8">
<title>Home Care Package Price Guide</title>
<link href="https://fonts.googleapis.com/css2?family=Arimo:wght@400;700&family=Carlito:wght@400;700&family=Montserrat:wght@400;600;700&display=swap" rel="stylesheet">
<style>
:root{
  --stage:#5e5e5e;
  --paper:#ffffff;
  --brand-blue:#3a2f91;
  --brand-red:#c93b2a;
  --row-light:#e7e4f3;
  --row-mid:#dcd8ec;
  --rule:#8d86c4;
  --ink:#1e1e1e;
}
*{box-sizing:border-box;margin:0;padding:0}
html,body{width:1200px;height:873px;overflow:hidden}
body{background:var(--stage);position:relative;font-family:"Montserrat",sans-serif;color:var(--ink)}
.page{position:absolute;top:112px;width:458px;height:648px;background:var(--paper);overflow:hidden}
.page--intro{left:120px}
.page--prices{left:615px}
.footer-band{position:absolute;left:0;right:0;bottom:0;height:26px;background:var(--brand-red);color:#fff;font-weight:600;font-size:10px;display:flex;align-items:center;justify-content:center;letter-spacing:.1px}

/* brand name block */
.brand{position:absolute;display:flex;flex-direction:column;align-items:center;gap:6px}
.brand__dot{width:30px;height:30px;border-radius:50%;background:var(--brand-red)}
.brand__name{font-family:"Arimo",sans-serif;font-weight:700;font-size:18px;color:var(--brand-blue);white-space:nowrap}
.page--intro .brand{left:0;right:0;top:52px}
.page--prices .brand{right:14px;top:500px;align-items:flex-end}

/* intro page */
.title{position:absolute;top:148px;left:0;right:0;text-align:center;font-family:"Arimo",sans-serif;font-weight:700;font-size:23.5px;line-height:26px;color:var(--brand-red)}
.intro-copy{position:absolute;left:52px;width:353px;top:216px;font-size:9.4px;line-height:12.7px}
.intro-copy p{margin-bottom:6px;text-align:justify}
.intro-copy h2{font-size:10px;font-weight:700;color:var(--brand-blue);margin-top:12px;line-height:12px;text-transform:uppercase}
.intro-copy .contact{margin-top:18px;text-align:left}

/* price tables */
.price-table{position:absolute;left:14px;width:429px;border-collapse:collapse;table-layout:fixed;font-family:"Carlito",sans-serif;font-size:6.4px;line-height:8.4px;color:#222}
.price-table td,.price-table th{border:0.6px solid var(--rule);padding:0 4px;vertical-align:middle;text-align:left}
.price-table th{background:var(--brand-blue);color:#fff;font-family:"Arimo",sans-serif;font-weight:700;border-color:var(--brand-blue)}
.price-table .th-title{font-size:9.2px;padding-left:9px}
.price-table .th-level{font-size:8.2px;text-align:center}
.price-table .th-time{font-size:6.6px;line-height:8.2px;vertical-align:top;padding-top:5px}
.price-table .th-title-top{vertical-align:top;padding-top:4px}
.light{background:var(--row-light)}
.mid{background:var(--row-mid)}
.white{background:#fff}
.center{text-align:center!important}
.indent{padding-left:41px!important}
.stack span{display:block;line-height:12.5px}
.fees{top:39px}
.cancel{top:117px;border:1px solid var(--brand-blue)}
.services{top:170px}

.effective{position:absolute;top:444px;left:0;right:0;text-align:center;font-family:"Carlito",sans-serif;font-weight:700;font-size:10px;color:var(--brand-blue)}
.get-in-touch{position:absolute;left:14px;top:546px;font-family:"Carlito",sans-serif;font-weight:700;font-size:8.5px;line-height:11.2px;color:#222}
.get-in-touch .label{color:var(--brand-blue)}
</style>
</head>
<body>

<section class="page page--intro">
  <div class="brand">
    <span class="brand__dot"></span>
    <span class="brand__name">Hearthside Home Care</span>
  </div>

  <h1 class="title">Home Care<br>Package Price Guide</h1>

  <div class="intro-copy">
    <p>Hearthside Home Care gives you the flexibility to choose the services that will best suit your needs and support your independence in your own home.</p>
    <p>You'll be selecting the home care services to assist you live the way you want, and stay in control of your own care.</p>

    <h2>What funding options are available?</h2>
    <p>Your home care services can be partly or fully funded by the government, through a Home Care Package (HCP), which you can apply for on the Aged Care Gateway Website.</p>
    <p>We're an approved HCP provider, so we're here for you, every step of the way.</p>

    <h2>What happens after I've been given a home care package?</h2>
    <p>Once your HCP has been allocated, we'll connect you with a friendly HHC Care Advisor to help you manage the services you choose.</p>

    <h2>How are home care services managed and delivered?</h2>
    <p>You'll have a team of care advisors, rostering team members and support workers. Your designated Care Advisor will assist with the management and set-up of your services, including roster, budget and initial care plan.</p>
    <p>Care plan will be periodically reviewed and updated according to your needs or priorities change.</p>

    <h2>We're always here to help</h2>
    <p>It's important to us that you receive the right services for your needs. You can talk with us to discuss making changes to your services at any time.</p>

    <p class="contact">Phone: 1800 412 770<br>Email: info@hearthsidecare.com.au</p>
  </div>

  <div class="footer-band">Hearthside Home Care</div>
</section>

<section class="page page--prices">
  <table class="price-table fees">
    <colgroup><col style="width:115px"><col style="width:143px"><col style="width:43px"><col style="width:43px"><col style="width:42px"><col style="width:43px"></colgroup>
    <tr style="height:22px">
      <th colspan="2" class="th-title">Fixed fees and charges</th>
      <th class="th-level">Level 1</th><th class="th-level">Level 2</th><th class="th-level">Level 3</th><th class="th-level">Level 4</th>
    </tr>
    <tr style="height:16px" class="light">
      <td colspan="2"></td><td colspan="4" class="center">Per month</td>
    </tr>
    <tr style="height:28px">
      <td class="white">Case Management Fee (Equivalent of 20% of the Home Care Package)</td>
      <td class="light">Activities relating to management of your care plan and services</td>
      <td class="white center">$171.19</td><td class="light center">$301.06</td><td class="white center">$655.18</td><td class="light center">$993.23</td>
    </tr>
  </table>

  <table class="price-table cancel mid">
    <colgroup><col style="width:115px"><col style="width:143px"><col style="width:171px"></colgroup>
    <tr style="height:32px">
      <td>Cancellation fees</td>
      <td class="stack"><span>More than 24 hours' notice</span><span>Less than 24 hours' notice</span></td>
      <td class="stack" style="padding-left:11px"><span>$0</span><span>Full Charge</span></td>
    </tr>
  </table>

  <table class="price-table services">
    <colgroup><col style="width:60px"><col style="width:105px"><col style="width:50px"><col style="width:50px"><col style="width:43px"><col style="width:45px"><col style="width:39px"><col style="width:38px"></colgroup>
    <tr style="height:53px">
      <th colspan="2" class="th-title th-title-top">Home care services available</th>
      <th class="th-time">Weekdays<br>6am-8pm<br>Mon-Fri</th>
      <th class="th-time">Afternoon<br>8pm-<br>12am<br>Mon-Fri</th>
      <th class="th-time">Nighttime<br>12am-<br>6am Mon-<br>Fri</th>
      <th class="th-time">Saturday</th>
      <th class="th-time">Sunday</th>
      <th class="th-time">Public<br>holidays</th>
    </tr>
    <tr style="height:20px" class="light">
      <td colspan="2"></td><td colspan="6" class="center">Per hour</td>
    </tr>
    <tr style="height:47px" class="light">
      <td class="white">With your Support Worker</td>
      <td>Cleaning, grocery shopping, meal prep, personal care</td>
      <td class="white center">$64.00</td><td class="center">$69.00</td><td class="white center">$75.00</td><td class="center">$93.00</td><td class="white center">$113.00</td><td class="center">$143.00</td>
    </tr>
    <tr style="height:34px" class="light">
      <td>With your Registered Nurse</td>
      <td class="stack"><span>Clinical support</span><span>Telehealth support</span></td>
      <td class="stack center"><span>$120.00</span><span>$120.00</span></td>
      <td class="stack center"><span>$130.00</span><span>$130.00</span></td>
      <td class="stack center"><span>$140.00</span><span>$140.00</span></td>
      <td class="stack center"><span>$168.00</span><span>$168.00</span></td>
      <td class="stack center"><span>$216.00</span><span>$216.00</span></td>
      <td class="stack center"><span>$264.00</span><span>$264.00</span></td>
    </tr>
    <tr style="height:26px" class="white">
      <td colspan="2" class="indent">Mileage - Travel as part of your service</td><td colspan="6" style="padding-left:13px">$1.30 per km</td>
    </tr>
    <tr style="height:26px" class="light">
      <td colspan="2" class="indent">Sleepover (Inactive)</td><td colspan="6" style="padding-left:13px">$245 per night (8 hours)</td>
    </tr>
    <tr style="height:20px" class="white">
      <td colspan="2" class="indent">Home maintenance/gardening</td><td colspan="6" style="padding-left:13px">Please discuss these services with your Case Manager</td>
    </tr>
    <tr style="height:20px" class="light">
      <td colspan="2" class="indent">Allied health support</td><td colspan="6" style="padding-left:13px">Please discuss these services with your Case Manager</td>
    </tr>
    <tr style="height:20px" class="white">
      <td colspan="2" class="indent">Short Term Home Respite</td><td colspan="6" style="padding-left:13px">Please discuss these services with your Case Manager</td>
    </tr>
  </table>

  <p class="effective">Prices are effective from 01 July 2023.</p>

  <div class="get-in-touch">
    <div class="label">Get in touch</div>
    <div>Phone: 1800 412 770</div>
    <div>Email: info@hearthsidecare.com.au</div>
  </div>

  <div class="brand">
    <span class="brand__dot"></span>
    <span class="brand__name">Hearthside Home Care</span>
  </div>

  <div class="footer-band">Hearthside Home Care</div>
</section>

</body>
</html>
```